Byte Crew - Settle Inn

A flyer to promote a service by Byte Crew that provides IT set up in home when moving house.

It should be for print format (A4, A5 and an email friendly version)

Logos, previous flyer, image all attached.

Please use black, green and white as base colours.Please change boys sweater/jumper in the photo to green to match the logo.

Byte Crew are bring a helpdesk to your front door, saving you time and money. With a variety of packages to suit your needs, the Byte Crew aims to tackle both small and complex issues from setting up a home network to servicing the needs of a growing company.

Target Market(s)

Consumers moving house, Relocation agents, Real Estate agents

Requirements
Must have
• Logo, image, text all attached
• Use of green, black and white
Nice to have
• Also have coloured ties if you want them for design

```html
<!DOCTYPE html>
<html lang="en">
<head>
<meta charset="utf-8">
<title>Byte Crew – Settle Inn flyer</title>
<link rel="stylesheet" href="https://fonts.googleapis.com/css2?family=Oswald:wght@500;700&family=Mulish:wght@400;600;800&display=swap">
<style>
  :root {
    --black: #050505;
    --green: #8fd61c;
    --white: #ffffff;
    --grey: #d8d8d8;
    --photo-dark: #2b3324;
    --photo-mid: #6f7d5a;
    --photo-light: #c9c0a8;
  }
  * { margin: 0; padding: 0; box-sizing: border-box; }
  html, body { width: 848px; height: 1200px; overflow: hidden; background: var(--black); }
  .flyer {
    position: relative; width: 848px; height: 1200px;
    background: var(--black); color: var(--white);
    font-family: "Mulish", Arial, sans-serif;
  }
  .rule { position: absolute; left: 0; width: 848px; height: 4px; background: var(--green); }
  .rule--top { top: 31px; }
  .rule--photo { top: 425px; }
  .hero-photo {
    position: absolute; top: 35px; left: 0; width: 848px; height: 390px;
    background:
      radial-gradient(ellipse 300px 260px at 560px 170px, var(--photo-light), transparent 70%),
      radial-gradient(ellipse 380px 140px at 560px 360px, #5fa02a, transparent 75%),
      linear-gradient(90deg, var(--photo-dark), var(--photo-mid) 55%, var(--photo-dark));
  }
  .headline {
    position: absolute; top: 44px; left: 40px; width: 320px;
    text-align: center; font-family: "Oswald", Impact, sans-serif; font-weight: 700;
    line-height: 1.02; color: var(--white); text-shadow: 0 2px 4px rgba(0,0,0,.5);
  }
  .headline span { display: block; }
  .headline .l1 { font-size: 58px; }
  .headline .l2 { font-size: 44px; }
  .headline .l3 { font-size: 44px; }
  .headline .l4 { font-size: 56px; color: var(--green); }
  .headline .accent { color: var(--green); }
  .reassure {
    position: absolute; top: 446px; left: 0; width: 848px; text-align: center;
    font-family: "Oswald", Impact, sans-serif; font-weight: 700;
  }
  .reassure .big { font-size: 70px; line-height: 1; display: block; }
  .reassure .line {
    display: flex; justify-content: center; align-items: center; gap: 22px;
    font-size: 32px; margin-top: 14px; font-weight: 500;
  }
  .brand-name { font-family: "Oswald", Impact, sans-serif; font-weight: 500; font-size: 40px; color: var(--white); }
  .intro {
    position: absolute; top: 628px; left: 30px; width: 788px; text-align: center;
    font-size: 21px; font-weight: 800; line-height: 1.5;
  }
  .features {
    position: absolute; top: 733px; left: 48px; width: 500px;
    list-style: none; font-size: 15.5px; line-height: 23px; color: var(--white);
  }
  .features li { position: relative; padding-left: 16px; }
  .features li::before { content: "•"; position: absolute; left: 0; }
  .badge { position: absolute; top: 718px; left: 552px; width: 262px; height: 262px; }
  .badge-text {
    position: absolute; top: 800px; left: 552px; width: 262px; text-align: center;
    color: var(--black); font-weight: 800; font-size: 29px; line-height: 1.15;
  }
  .badge-text .price { display: block; font-size: 44px; margin-top: 4px; }
  .footnotes {
    position: absolute; top: 1133px; left: 64px; font-size: 9.5px; line-height: 14px; color: var(--grey);
  }
  .booking { position: absolute; top: 1018px; left: 536px; width: 300px; }
  .booking .cta { font-size: 58px; font-weight: 600; line-height: 1; }
  .booking .web { color: var(--green); font-size: 22px; font-weight: 800; margin-top: 6px; }
  .booking .contact { font-size: 17px; margin-top: 9px; }
  .booking .contact b { font-weight: 800; }
</style>
</head>
<body>
<main class="flyer">
  <div class="rule rule--top"></div>
  <div class="hero-photo" role="img" aria-label="Photo of a worried boy in glasses and a green jumper holding two network cables"></div>
  <div class="rule rule--photo"></div>

  <h1 class="headline">
    <span class="l1">Can’t</span>
    <span class="l2">remember</span>
    <span class="l3"><span class="accent" style="display:inline">what</span> to plug in</span>
    <span class="l4">where?</span>
  </h1>

  <section class="reassure">
    <span class="big">Do not fear...</span>
    <div class="line"><span>the</span><span class="brand-name">Byte Crew</span><span>is here!</span></div>
  </section>

  <p class="intro">We take all the pain out of moving house and get you set-up,<br>online and connected before you can say the word Geek.</p>

  <ul class="features">
    <li>Pre-visit online assessment to ensure maximum<br>use of our Geek’s time</li>
    <li>Ready:&nbsp; IT Health Check and Audit report</li>
    <li>Set:&nbsp; Connection of your wireless network for user access<br>including passwords and parental control if desired</li>
    <li>Go: Set up of 3 computers and 1 printer</li>
    <li>Expanding the family: Connection of one additional<br>device eg&nbsp; media box, tablet, games console, Smart TV*</li>
    <li>Updating of software and virus security check</li>
    <li>Byte Crew Membership</li>
    <li>Includes travel cost and up to 4 hours of a Geek’s<br>time in your house</li>
    <li>1 month free on Crew@Home Packages**</li>
    <li>Awesome Byte Crew fridge magnet</li>
  </ul>

  <svg class="badge" viewBox="0 0 262 262" aria-hidden="true">
    <g fill="#8fd61c" transform="translate(131 131)">
      <rect x="-94" y="-94" width="188" height="188"/>
      <rect x="-94" y="-94" width="188" height="188" transform="rotate(11.25)"/>
      <rect x="-94" y="-94" width="188" height="188" transform="rotate(22.5)"/>
      <rect x="-94" y="-94" width="188" height="188" transform="rotate(33.75)"/>
      <rect x="-94" y="-94" width="188" height="188" transform="rotate(45)"/>
      <rect x="-94" y="-94" width="188" height="188" transform="rotate(56.25)"/>
      <rect x="-94" y="-94" width="188" height="188" transform="rotate(67.5)"/>
      <rect x="-94" y="-94" width="188" height="188" transform="rotate(78.75)"/>
    </g>
  </svg>
  <div class="badge-text">WELCOME<br>HOME CREW<span class="price">$425</span></div>

  <div class="footnotes">
    *Each additional device set-up is charged at $35<br>
    ** Based on our annual packages and If signed within 14 days
  </div>

  <section class="booking">
    <div class="cta">Book now</div>
    <div class="web">www.bytecrew.asia</div>
    <div class="contact">Singapore hotline <b>6100 2345</b></div>
    <div class="contact">email <b>booking@bytecrew.asia</b></div>
  </section>
</main>
</body>
</html>
```